sign business needs card design

I need a very clean design for my business card.
It is a sign company. Banners By Noon is the name of the business.
Our colors are orange, yellow. But I want a very professional card.
But you can use any colors. I like a black background with orange letters or a white back with a clean look. No cartoon or kiddy looking print. The info. I need on the card is as follows.
Banners By Noon
318.514.7702 ph.
318.514.7739 fax.
email.bannersbynoon@velmora.net
web.bannersbynooninc.example
4172 N. Calloway Ridge Ste. 2b
Dale Kessner

```html
<!DOCTYPE html>
<html lang="en">
<head>
<meta charset="utf-8">
<title>Banners By Noon – Business Card</title>
<link rel="stylesheet" href="https://fonts.googleapis.com/css2?family=Open+Sans:wght@400&display=swap">
<style>
  :root {
    --stage: #000000;
    --paper: #ffffff;
    --leaf: #94d351;
    --ink-light: #ffffff;
  }
  html, body {
    margin: 0;
    padding: 0;
    width: 1200px;
    height: 900px;
    overflow: hidden;
    background: var(--stage);
    font-family: "Open Sans", "Segoe UI", sans-serif;
  }
  .card {
    position: absolute;
    left: 282px;
    top: 250px;
    width: 639px;
    height: 351px;
    background: var(--paper);
    overflow: hidden;
  }
  .accent-band {
    position: absolute;
    left: 27px;
    top: 0;
    width: 170px;
    height: 100%;
    background: var(--leaf);
  }
  .rule {
    position: absolute;
    left: 27px;
    top: 296px;
    width: 612px;
    height: 2px;
    background: var(--leaf);
  }
  .phone-list {
    position: absolute;
    left: 34px;
    top: 40px;
    margin: 0;
    color: var(--ink-light);
    font-size: 16px;
    line-height: 35px;
  }
  .phone-list .label {
    font-size: 15px;
    margin-right: 4px;
  }
  .phone-list .label.fax {
    font-size: 14px;
  }
  .online-list {
    position: absolute;
    left: 334px;
    top: 40px;
    margin: 0;
    color: var(--leaf);
    font-size: 16px;
    line-height: 29px;
  }
  .online-list .label {
    display: inline-block;
    width: 64px;
    font-size: 14px;
  }
  .business-name {
    position: absolute;
    left: 0;
    top: 0;
    width: 639px;
    height: 351px;
  }
  .business-name text {
    font-family: "Open Sans", "Segoe UI", sans-serif;
    font-size: 44px;
  }
  .address-line {
    position: absolute;
    left: 210px;
    top: 303px;
    margin: 0;
    color: var(--leaf);
    font-size: 16px;
    white-space: nowrap;
  }
</style>
</head>
<body>
  <div class="card">
    <div class="accent-band"></div>
    <div class="rule"></div>

    <p class="phone-list">
      <span class="label">Ph.</span>318.514.7702<br>
      <span class="label fax">Fax.</span>318.514.7739
    </p>

    <p class="online-list">
      <span class="label">Emil :</span>bannersbynoon@velmora.net<br>
      <span class="label">Web :</span>bannersbynooninc.example
    </p>

    <svg class="business-name" viewBox="0 0 639 351" aria-label="Banners By Noon">
      <defs>
        <clipPath id="band-area">
          <rect x="27" y="0" width="170" height="351"/>
        </clipPath>
      </defs>
      <text x="61" y="173" fill="var(--leaf)">Banners By Noon</text>
      <text x="61" y="173" fill="var(--ink-light)" clip-path="url(#band-area)">Banners By Noon</text>
    </svg>

    <p class="address-line">4172 N. Calloway Ridge Ste. 2b Dale Kessner</p>
  </div>
</body>
</html>
```